Assisted living facility needs a business card design

We need a business card design for an assisted living facility in Los Angeles. We have a logo selected but we would like a business card design that will leave a lasting impression on families looking to place their elderly loved ones in our care as well as on other facility providers who may refer their elderly residents to our facility.

```html
<!DOCTYPE html>
<html lang="en">
<head>
<meta charset="utf-8">
<title>Harborview Gardens Senior Living – Business Card</title>
<link rel="stylesheet" href="https://fonts.googleapis.com/css2?family=Arimo:ital,wght@0,400;0,700;1,400&display=swap">
<style>
  :root {
    --page-bg: #e6e7e9;
    --card-bg: #ffffff;
    --brand-blue: #1f6fc0;
    --ink: #1c1c1c;
    --muted: #555a60;
    --rule: #2a2a2a;
  }
  * { box-sizing: border-box; margin: 0; padding: 0; }
  html, body {
    width: 1200px; height: 960px; overflow: hidden;
    background: var(--page-bg);
    font-family: "Arimo", Arial, sans-serif;
  }
  .sheet {
    width: 1200px; height: 960px;
    display: flex; flex-direction: column; align-items: center; justify-content: center;
    gap: 50px;
  }
  .card {
    position: relative;
    width: 700px; height: 400px;
    background: var(--card-bg);
    border-radius: 22px;
    box-shadow: 0 6px 18px rgba(0,0,0,0.12);
  }
  .wordmark {
    display: flex; align-items: center; gap: 12px;
    color: var(--brand-blue);
    font-weight: 400;
    text-transform: uppercase;
    letter-spacing: 0.08em;
    line-height: 1.1;
  }
  .wordmark-dot {
    flex: none;
    border-radius: 50%;
    background: var(--brand-blue);
  }
  /* back */
  .card-back { display: flex; align-items: center; justify-content: center; }
  .card-back .wordmark { font-size: 34px; }
  .card-back .wordmark-dot { width: 22px; height: 22px; }
  /* front */
  .holder { position: absolute; left: 44px; top: 42px; }
  .holder-name { color: var(--brand-blue); font-weight: 700; font-size: 26px; }
  .holder-title { color: var(--muted); font-style: italic; font-size: 16px; margin-top: 3px; }
  .card-front .wordmark {
    position: absolute; right: 44px; top: 138px;
    font-size: 24px;
  }
  .card-front .wordmark-dot { width: 16px; height: 16px; }
  .contact {
    position: absolute; left: 44px; right: 44px; bottom: 42px;
    color: var(--ink); font-size: 17px;
  }
  .contact-row { display: flex; justify-content: space-between; padding-bottom: 10px; }
  .contact-sep { color: var(--muted); }
  .contact-rule { height: 1px; background: var(--rule); }
  .contact-address { text-align: center; padding-top: 12px; }
</style>
</head>
<body>
<main class="sheet">
  <section class="card card-back" aria-label="Card back">
    <div class="wordmark"><span class="wordmark-dot"></span><span>Harborview Gardens<br>Senior Living</span></div>
  </section>

  <section class="card card-front" aria-label="Card front">
    <div class="holder">
      <p class="holder-name">Daniel Hartley</p>
      <p class="holder-title">President</p>
    </div>
    <div class="wordmark"><span class="wordmark-dot"></span><span>Harborview Gardens<br>Senior Living</span></div>
    <div class="contact">
      <div class="contact-row">
        <span>(555) 0142-7788</span><span class="contact-sep">|</span>
        <span>name@harborviewgardens.com</span><span class="contact-sep">|</span>
        <span>www.harborviewgardens.com</span>
      </div>
      <div class="contact-rule"></div>
      <p class="contact-address">2190 Linden Court, Maple Grove, CA 90012</p>
    </div>
  </section>
</main>
</body>
</html>
```